Business card design for international hub site

I need a business card design with the logo attached. Although the site is for the teenage audience (it is about the high school graduation ball, the Prom), the business card is for professional use to be given to professional contacts (B2B), such as suppliers and partners, so it needs to look professional (but also girly, glamours and clean).

Target Market(s)

B2B

Industry/Entity Type

Media

Colors
eea4c8
f9d9e8
e667a6
9d9d9d
1b1b1b

Requirements
Must have
• Space for Name, Tile, Address, Phone, email and website.
Should not have
• Photo

```html
<!DOCTYPE html>
<html lang="en">
<head>
<meta charset="utf-8">
<title>Gala Hum — Business Card</title>
<link rel="stylesheet" href="https://fonts.googleapis.com/css2?family=Tinos:wght@400;700&display=swap">
<style>
  :root {
    --pink-soft: #f9d9e8;
    --pink-light: #eea4c8;
    --pink-bright: #e667a6;
    --pink-deep: #b35a8c;
    --grey: #9d9d9d;
    --ink: #1b1b1b;
    --paper: #ffffff;
    --backdrop: #ecebea;
  }
  * { box-sizing: border-box; margin: 0; padding: 0; }
  html, body { width: 1200px; height: 800px; overflow: hidden; }
  body {
    background: var(--backdrop);
    font-family: "Tinos", "Times New Roman", serif;
    color: var(--ink);
    position: relative;
  }
  .card {
    position: absolute;
    width: 520px;
    height: 300px;
    border-radius: 3px;
    box-shadow: 0 8px 24px rgba(0,0,0,.18);
    overflow: hidden;
  }
  .card--front {
    left: 50px; top: 130px;
    background: var(--paper);
    display: flex; align-items: center; justify-content: center;
  }
  .card--back {
    left: 630px; top: 370px;
    background: linear-gradient(120deg, var(--pink-deep) 0%, var(--pink-bright) 100%);
  }
  .brand-name {
    font-family: "Tinos", "Times New Roman", serif;
    font-weight: 400;
    color: var(--grey);
    letter-spacing: 1px;
    white-space: nowrap;
  }
  .card--front .brand-name { font-size: 58px; }
  .brand-badge {
    position: absolute;
    left: 28px; bottom: -28px;
    width: 210px; height: 210px;
    border-radius: 50%;
    background: var(--paper);
    display: flex; align-items: center; justify-content: center;
  }
  .brand-badge .brand-name { font-size: 34px; }
  .contact {
    position: absolute;
    left: 280px; top: 42px;
    font-size: 14px;
    line-height: 1.25;
  }
  .contact__name { font-weight: 700; font-size: 19px; }
  .contact__title { font-size: 14px; margin-bottom: 18px; }
  .contact__address { margin-bottom: 16px; }
  .contact__row { display: flex; align-items: center; gap: 9px; margin-bottom: 6px; }
  .contact__icon {
    width: 22px; height: 22px; border-radius: 50%;
    background: var(--pink-soft);
    display: flex; align-items: center; justify-content: center;
  }
  .contact__web { margin-top: 12px; }
</style>
</head>
<body>
  <section class="card card--front" aria-label="Card front">
    <span class="brand-name">gala hum</span>
  </section>

  <section class="card card--back" aria-label="Card back">
    <div class="brand-badge"><span class="brand-name">gala hum</span></div>
    <div class="contact">
      <p class="contact__name">Clara Hughes</p>
      <p class="contact__title">Director</p>
      <p class="contact__address">48, Linden Court, Maple<br>Street, CA 90210</p>
      <p class="contact__row">
        <span class="contact__icon">
          <svg width="12" height="12" viewBox="0 0 12 12"><rect x="3" y="1" width="6" height="10" rx="1" fill="none" stroke="#b35a8c" stroke-width="1.4"/><line x1="5" y1="9" x2="7" y2="9" stroke="#b35a8c" stroke-width="1.2"/></svg>
        </span>
        555 . 201 .4478
      </p>
      <p class="contact__row">
        <span class="contact__icon">
          <svg width="12" height="12" viewBox="0 0 12 12"><rect x="1" y="3" width="10" height="7" fill="none" stroke="#b35a8c" stroke-width="1.3"/><polyline points="1,3 6,7 11,3" fill="none" stroke="#b35a8c" stroke-width="1.3"/></svg>
        </span>
        hello@galahum.com
      </p>
      <p class="contact__web">www.galahum.com</p>
    </div>
  </section>
</body>
</html>
```